Rally 84 Training is our company name. and instruction

We provide emergency medical training for CPR (Cardiopulmonary Resuscitation) /AED (Automated External Defibrillation) , BLS (Basic Life Support, First Aid, Bloodborne Pathogens
We travel to the client, give certified (CVL) Continental Vitality League (CVL) instruction for job/industry certification in the areas listed.
CVL Kin and Neighbors noncertified instruction

Target Market(s)

Medical professionals, job required certification

Industry/Entity Type

Medical And Science

Contact Information for Business Card

Logo
Phone, email, address, website address, FB, Instagram

Font styles to use
Serif
Sans Serif

Colors
fff2fe
ff1b2f

Requirements
Must have
• Logo
Course taught: CPR (Cardiopulmonary Resuscitation)
AED (Automated External Defibrillation)
First Aid
BLS (Basic Life Support)
Bloodborne Pathogens
Offsite instruction - we come to you
Nice to have
• Red/Black scheme
Possible ecg/heart rhythm design
Should not have
• Cartoon images

```html
<!DOCTYPE html>
<html lang="en">
<head>
<meta charset="utf-8">
<title>Rally 84 Training – Business Card</title>
<link rel="stylesheet" href="https://fonts.googleapis.com/css2?family=Cinzel:wght@700&family=Arimo:wght@400;700&display=swap">
<style>
  :root {
    --red: #ff1b2f;
    --black: #141414;
    --gold: #e3b835;
    --grey: #b9b9b9;
    --white: #fff2fe;
    --backdrop: #3a3a3a;
    --rule: #2e2e2e;
  }
  * { box-sizing: border-box; margin: 0; padding: 0; }
  html, body { width: 1200px; height: 1015px; overflow: hidden; }
  body {
    background: var(--backdrop);
    font-family: "Arimo", Arial, sans-serif;
    display: flex; flex-direction: column; align-items: center;
    gap: 30px; padding-top: 35px;
  }
  .card {
    width: 800px; height: 457px; background: var(--black);
    position: relative; overflow: hidden;
    box-shadow: 0 10px 28px rgba(0,0,0,.55);
  }
  /* back side */
  .card-back .top-band {
    height: 86px; background: var(--red);
    display: flex; align-items: center; justify-content: center;
  }
  .section-title {
    font-family: "Cinzel", Georgia, serif; color: var(--gold);
    font-size: 27px; letter-spacing: 1px;
  }
  .course-list {
    list-style: none; text-align: center; margin-top: 58px;
    color: var(--grey); font-size: 21px; line-height: 1.55;
    text-transform: uppercase; letter-spacing: .3px;
  }
  /* front side */
  .card-front .bottom-band {
    position: absolute; left: 0; right: 0; bottom: 0; height: 92px;
    background: var(--red);
  }
  .brand {
    position: absolute; left: 0; top: 0; width: 390px; height: 365px;
    display: flex; align-items: center; justify-content: center;
  }
  .brand-name {
    font-family: "Arimo", Arial, sans-serif; color: var(--white);
    font-size: 30px; font-weight: 700; letter-spacing: .3px;
  }
  .divider {
    position: absolute; left: 390px; top: 30px; width: 1px; height: 300px;
    background: var(--rule);
  }
  .contact { position: absolute; left: 430px; top: 62px; color: var(--white); }
  .person-name {
    font-family: "Cinzel", Georgia, serif; color: var(--gold);
    font-size: 26px; letter-spacing: .5px;
  }
  .person-role { font-size: 18px; margin-top: 2px; margin-bottom: 18px; }
  .contact-line { display: flex; align-items: center; gap: 9px; font-size: 17px; line-height: 1.5; }
  .contact-line svg { width: 17px; height: 17px; flex: none; }
  .address { font-size: 17px; line-height: 1.4; margin-top: 14px; color: var(--grey); }
  .social {
    position: absolute; left: 390px; right: 0; top: 320px;
    display: flex; align-items: center; justify-content: center; gap: 10px;
    color: var(--white); font-size: 15px;
  }
  .social-dot { width: 24px; height: 24px; border: 2px solid var(--white); border-radius: 50%; }
</style>
</head>
<body>
  <section class="card card-back">
    <div class="top-band"><h2 class="section-title">COURSE TAUGHT</h2></div>
    <ul class="course-list">
      <li>CPR (Cardiopulmonary Resuscitation)</li>
      <li>AED (Automated External Defibrillation)</li>
      <li>First Aid</li>
      <li>BLS (Basic Life Support)</li>
      <li>Bloodborne Pathogens</li>
      <li>Offsite Instruction - We Come To You</li>
    </ul>
  </section>

  <section class="card card-front">
    <div class="brand">
      <span class="brand-name">Rally 84 Training</span>
    </div>
    <div class="divider"></div>
    <div class="contact">
      <h1 class="person-name">MARCUS ELLERY</h1>
      <p class="person-role">Managing Director</p>
      <p class="contact-line">
        <svg viewBox="0 0 20 20"><rect x="1" y="1" width="18" height="18" rx="3" fill="none" stroke="#e3b835" stroke-width="2"/><path d="M6 5c0 5 4 9 9 9l1-2-3-1-1 1c-2-1-3-2-4-4l1-1-1-3z" fill="#e3b835"/></svg>
        044-555 018 284
      </p>
      <p class="contact-line">
        <svg viewBox="0 0 20 20"><rect x="1" y="4" width="18" height="12" fill="#e3b835"/><path d="M1 4l9 7 9-7" fill="none" stroke="#141414" stroke-width="1.6"/></svg>
        info@rally84mail.com
      </p>
      <p class="contact-line">
        <svg viewBox="0 0 20 20"><circle cx="10" cy="10" r="8.5" fill="none" stroke="#e3b835" stroke-width="2"/><ellipse cx="10" cy="10" rx="3.5" ry="8.5" fill="none" stroke="#e3b835" stroke-width="1.5"/><path d="M2 10h16" stroke="#e3b835" stroke-width="1.5"/></svg>
        www.rally84training.com
      </p>
      <p class="address">84 Harbor Lane, Suite 2<br>45480, Westmere</p>
    </div>
    <div class="social"><span class="social-dot"></span>Rally 84 Online</div>
    <div class="bottom-band"></div>
  </section>
</body>
</html>
```